Tavok Construction we build lodges in Botswana

We need a Design Layout only with Categories where we can update each projects photos.... We have a web address and a host - tavok.construction

```html
<!DOCTYPE html>
<html lang="en">
<head>
<meta charset="utf-8">
<title>Tavok Construction</title>
<link href="https://fonts.googleapis.com/css2?family=Roboto:wght@400;500;700;900&family=Lato:wght@400;700&display=swap" rel="stylesheet">
<style>
:root{
  --red:#ff0000;
  --ink:#1d1d1d;
  --text:#555555;
  --soft:#f5f5f5;
  --white:#ffffff;
  --dark:#333333;
  --darker:#2a2a2a;
  --blue:#1565c0;
  --line:#e4e4e4;
}
*{margin:0;padding:0;box-sizing:border-box}
html,body{width:1200px;height:4663px;overflow:hidden}
body{font-family:"Lato",sans-serif;color:var(--text);background:var(--white);position:relative}
.section{position:absolute;left:0;width:1200px}
.abs{position:absolute}
.heading{font-family:"Roboto",sans-serif;font-weight:700;color:var(--ink);text-transform:uppercase;text-align:center;font-size:30px;letter-spacing:.5px}
.btn{position:absolute;background:var(--red);color:var(--white);font-family:"Roboto",sans-serif;font-weight:700;font-size:15px;text-transform:uppercase;display:flex;align-items:center;justify-content:center;letter-spacing:.5px}
.para{font-size:15px;line-height:25px;color:var(--text)}
.photo{position:absolute}

/* hero */
.hero{top:0;height:710px;background:linear-gradient(180deg,#6f8fae 0%,#9fb4c4 35%,#7a6045 60%,#5a6a3a 85%,#3f4a2a 100%)}
.hero-shade{position:absolute;inset:0;background:rgba(0,0,0,.22)}
.brand{position:absolute;left:40px;top:22px;display:flex;align-items:center;gap:10px;color:var(--white);font-family:"Roboto",sans-serif;font-weight:700;font-size:18px;text-transform:uppercase}
.brand-dot{width:18px;height:18px;border-radius:50%;background:var(--white)}
.nav{position:absolute;right:40px;top:40px;display:flex;gap:28px;font-family:"Roboto",sans-serif;font-size:16px;color:var(--white)}
.nav .active{background:var(--red);padding:0 10px;margin-right:-14px}
.hero-kicker{position:absolute;top:262px;width:100%;text-align:center;color:var(--white);font-family:"Roboto",sans-serif;font-weight:700;font-size:30px;text-transform:uppercase}
.hero-title{position:absolute;top:298px;width:100%;text-align:center;color:var(--white);font-family:"Roboto",sans-serif;font-weight:900;font-size:74px;text-transform:uppercase;letter-spacing:1px}
.hero-sub{position:absolute;top:390px;width:100%;text-align:center;color:var(--white);font-size:16px}
.hero-bar{position:absolute;top:622px;left:40px;right:40px;display:flex;align-items:center;color:var(--white);font-size:15px}
.hero-bar .phone{margin-left:118px}
.follow{margin-left:auto;display:flex;align-items:center;gap:20px}
.sq{width:14px;height:14px;background:var(--white);border-radius:3px;display:inline-block}
.sq.red{background:var(--red)}
.mouse{position:absolute;left:588px;top:615px}

/* about */
.about{top:710px;height:330px;background:var(--soft)}

/* services */
.services{top:1040px;height:1740px;background:var(--white)}
.svc-title{position:absolute;font-family:"Roboto",sans-serif;font-weight:700;font-size:28px;color:var(--ink);text-transform:uppercase;letter-spacing:.5px}
.svc-text{position:absolute;width:240px}
.link{position:absolute;color:var(--red);font-family:"Roboto",sans-serif;font-weight:700;font-size:14px;text-transform:uppercase;text-decoration:underline}

/* projects */
.projects{top:2780px;height:885px;background:var(--soft)}
.grid{position:absolute;left:38px;top:155px;width:1124px;display:grid;grid-template-columns:repeat(3,1fr);gap:6px}
.tile{height:272px;position:relative}
.tile-overlay{position:absolute;inset:0;background:rgba(0,0,0,.45);color:var(--white);padding:70px 28px}
.tile-overlay h3{font-family:"Roboto",sans-serif;font-size:19px;text-transform:uppercase;margin-bottom:10px}
.tile-overlay p{font-size:14px;line-height:22px;width:260px}
.tile-overlay span{display:inline-block;margin-top:16px;font-family:"Roboto",sans-serif;font-weight:700;font-size:15px;text-decoration:underline}

/* contact */
.contact{top:3665px;height:535px;background:var(--white)}
.field{position:absolute;border:1px solid var(--line);background:var(--white);font-size:14px;color:#aaa;padding:14px 16px;font-style:italic}

/* footer */
.footer{top:4200px;height:463px;background:var(--dark);color:#ddd}
.foot-h{position:absolute;top:75px;font-family:"Roboto",sans-serif;font-weight:700;font-size:19px;color:var(--white);text-transform:uppercase}
.foot-list{position:absolute;top:130px;list-style:none;font-size:14px;color:#ddd}
.foot-list li{height:40px;display:flex;align-items:center;gap:16px}
.foot-list .arrow{color:var(--red)}
.useful li{align-items:flex-start;height:auto;margin-bottom:16px;line-height:20px}
.ico{width:16px;flex:none;margin-top:2px}
.email-box{position:absolute;left:892px;top:196px;width:270px;height:52px;border:1px solid #777;color:#ccc;font-size:14px;padding:16px;font-style:italic}
.bottom{position:absolute;top:352px;left:40px;right:40px;border-top:1px solid #555;padding-top:40px;display:flex;justify-content:space-between;font-size:14px;color:#ddd}
</style>
</head>
<body>

<section class="section hero">
  <div class="photo" role="img" aria-label="Timber log lodges with a wooden path and staircase on a green lawn under a cloudy sky" style="inset:0"></div>
  <div class="hero-shade"></div>
  <div class="brand"><span class="brand-dot"></span>Tavok Construction</div>
  <nav class="nav">
    <span class="active">Home</span><span>About us</span><span>Services</span><span>Projects</span><span>Contact us</span>
  </nav>
  <p class="hero-kicker">A quality line of</p>
  <h1 class="hero-title">Construction</h1>
  <p class="hero-sub">we build lodges in Botswana</p>
  <div class="btn" style="left:500px;top:428px;width:200px;height:56px">Read more</div>
  <div class="hero-bar">
    <span>Email : info@tavokconstruction.com</span>
    <span class="phone">Phone : (+267) 555 014 2</span>
    <div class="follow"><span>Follow us :</span><span class="sq red"></span><span class="sq"></span><span class="sq"></span><span class="sq"></span><span class="sq"></span></div>
  </div>
  <svg class="mouse" width="24" height="44" viewBox="0 0 24 44"><rect x="2" y="2" width="20" height="40" rx="10" fill="none" stroke="#fff" stroke-width="2"/><rect x="10.5" y="10" width="3" height="9" rx="1.5" fill="#fff"/></svg>
</section>

<section class="section about">
  <h2 class="heading abs" style="top:20px;width:100%">About us</h2>
  <p class="para abs" style="left:210px;top:100px;width:780px;text-align:center">Lorem Ipsum is simply dummy text of the printing and typesetting industry. Lorem Ipsum has been the industry's standard dummy text ever since the 1500s, when an unknown printer took a galley of type and scrambled it to make a type specimen book.</p>
  <div class="btn" style="left:503px;top:212px;width:195px;height:56px">Read more</div>
</section>

<section class="section services">
  <h2 class="heading abs" style="top:80px;width:100%">Our services</h2>

  <div class="photo" role="img" aria-label="Timber frame of a new wooden building against a blue sky" style="left:208px;top:190px;width:474px;height:340px;background:linear-gradient(160deg,#3f7fd0,#9dc3ea 45%,#b98a52 70%,#7a5530)"></div>
  <h3 class="svc-title" style="left:740px;top:205px">Design &amp; Build</h3>
  <p class="para svc-text" style="left:740px;top:265px">Lorem Ipsum is simply dummy text of the printing and typesetting industry. Lorem Ipsum has been the industry's standard dummy text ever since the 1500s, when an unknown printer took a galley of type and scrambled it to make a type specimen book.</p>
  <div class="btn" style="left:740px;top:450px;width:195px;height:56px">Learn more</div>

  <h3 class="svc-title" style="left:205px;top:640px">Renovation</h3>
  <p class="para svc-text" style="left:205px;top:700px">Lorem Ipsum is simply dummy text of the printing and typesetting industry. Lorem Ipsum has been the industry's standard dummy text ever since the 1500s, when an unknown printer took a galley of type and scrambled it to make a type specimen book.</p>
  <div class="btn" style="left:205px;top:885px;width:195px;height:56px">Learn more</div>
  <div class="photo" role="img" aria-label="White house with a dark roof wrapped in scaffolding beside green trees" style="left:530px;top:620px;width:475px;height:335px;background:linear-gradient(180deg,#4a86d8,#a9c9ee 45%,#e8e8e8 62%,#5f8f3c 85%)"></div>

  <div class="photo" role="img" aria-label="Engineers in a bright office reviewing construction plans on a table" style="left:208px;top:1065px;width:474px;height:575px;background:linear-gradient(180deg,#e8ecef,#d6dbe0 50%,#f3f4f5)"></div>
  <div class="abs" style="left:678px;top:1125px;width:5px;height:475px;background:var(--blue)"></div>
  <h3 class="svc-title" style="left:740px;top:1085px">Project managemnt</h3>
  <p class="para svc-text" style="left:740px;top:1145px">Lorem Ipsum is simply dummy text of the printing and typesetting industry. Lorem Ipsum has been the industry's standard dummy text ever since the 1500s, when an unknown printer took a galley of type and scrambled it to make a type specimen book.</p>
  <div class="btn" style="left:740px;top:1325px;width:195px;height:56px">Learn more</div>
  <span class="link" style="left:740px;top:1578px">View all our services ...</span>
</section>

<section class="section projects">
  <h2 class="heading abs" style="top:65px;width:100%">Latest projects</h2>
  <div class="grid">
    <div class="tile" role="img" aria-label="Cosy wooden bedroom with a chandelier" style="background:linear-gradient(160deg,#8a5a35,#d7b48a 55%,#f1e4d2)"></div>
    <div class="tile" role="img" aria-label="Lodge in Botswana at dusk" style="background:linear-gradient(180deg,#0f2a40,#2d4f5a 60%,#3a5a2a)">
      <div class="tile-overlay"><h3>Lodge in Botswana</h3><p>Lorem Ipsum is simply dummy text of the printing and typesetting industry.</p><span>VIEW PROJECT...</span></div>
    </div>
    <div class="tile" role="img" aria-label="Log cabin with a porch under a blue sky" style="background:linear-gradient(180deg,#3c7fd6,#9ec6f0 45%,#9a5a2c 65%,#5d8a3a)"></div>
    <div class="tile" role="img" aria-label="Two-storey timber house among trees" style="background:linear-gradient(180deg,#5d94d8,#a9cdea 35%,#7a4a28 60%,#4d7a2c)"></div>
    <div class="tile" role="img" aria-label="Wooden farmhouse on a green lawn" style="background:linear-gradient(180deg,#2f6fcf,#bcd8f2 40%,#6d4a30 62%,#58913a)"></div>
    <div class="tile" role="img" aria-label="Bright open-plan living room with timber finishes" style="background:linear-gradient(160deg,#f2f0ec,#d8cfc3 50%,#8c6a4c)"></div>
  </div>
  <div class="btn" style="left:503px;top:765px;width:195px;height:56px">View all</div>
</section>

<section class="section contact">
  <h2 class="heading abs" style="top:95px;width:100%">Contact us</h2>
  <div class="field" style="left:320px;top:175px;width:275px;height:52px">Full Name</div>
  <div class="field" style="left:605px;top:175px;width:275px;height:52px">Phone #</div>
  <div class="field" style="left:320px;top:235px;width:560px;height:52px">Email Address</div>
  <div class="field" style="left:320px;top:295px;width:560px;height:105px">Message</div>
  <div class="btn" style="left:320px;top:407px;width:560px;height:56px">Submit now</div>
</section>

<footer class="section footer">
  <div class="abs" style="left:40px;top:108px;display:flex;align-items:center;gap:10px;font-family:'Roboto',sans-serif;font-weight:700;font-size:14px;color:var(--white);text-transform:uppercase"><span style="width:14px;height:14px;background:var(--red)"></span>Tavok Construction</div>
  <p class="abs" style="left:40px;top:178px;width:250px;font-size:14px;line-height:22px">Lorem Ipsum is simply dummy text of the printing and typesetting industry.</p>
  <span class="abs" style="left:40px;top:232px;color:var(--red);font-family:'Roboto',sans-serif;font-weight:700;font-size:14px;text-decoration:underline">READ MORE...</span>
  <div class="abs" style="left:40px;top:288px;display:flex;gap:18px"><span class="sq red" style="width:12px;height:12px"></span><span class="sq" style="width:12px;height:12px"></span><span class="sq" style="width:12px;height:12px"></span><span class="sq" style="width:12px;height:12px"></span><span class="sq" style="width:12px;height:12px"></span></div>

  <h4 class="foot-h" style="left:355px">Quick links</h4>
  <ul class="foot-list" style="left:358px">
    <li><span class="arrow">›</span>Home</li><li><span class="arrow">›</span>About us</li><li><span class="arrow">›</span>Services</li><li><span class="arrow">›</span>Projects</li><li><span class="arrow">›</span>Contact us</li>
  </ul>

  <h4 class="foot-h" style="left:588px">Useful links</h4>
  <ul class="foot-list useful" style="left:588px;width:270px">
    <li><svg class="ico" viewBox="0 0 16 16"><path d="M3 1h3l1.5 4-2 1.2a9 9 0 0 0 4.3 4.3L11 8.5l4 1.5v3a2 2 0 0 1-2 2A12 12 0 0 1 1 3a2 2 0 0 1 2-2z" fill="#2f80ed"/></svg>(+267) 555 014 2</li>
    <li><svg class="ico" viewBox="0 0 16 16"><rect x="1" y="3" width="14" height="10" rx="1" fill="#2f80ed"/><path d="M1.5 4l6.5 5 6.5-5" stroke="#333" stroke-width="1.4" fill="none"/></svg>info@tavokconstruction.com</li>
    <li><svg class="ico" viewBox="0 0 16 16"><path d="M8 1a5 5 0 0 0-5 5c0 4 5 9 5 9s5-5 5-9a5 5 0 0 0-5-5z" fill="#2f80ed"/><circle cx="8" cy="6" r="2" fill="#333"/></svg>18 Kgale Rise,<br>Gaborone, BW 00267</li>
    <li><svg class="ico" viewBox="0 0 16 16"><circle cx="8" cy="8" r="7" fill="#2f80ed"/><path d="M8 4v4l3 2" stroke="#333" stroke-width="1.6" fill="none"/></svg>Saturday to Monday :<br>8.00 AM to 10.00 PM<br>Sunday Close</li>
  </ul>

  <h4 class="foot-h" style="left:892px">Newsletter</h4>
  <p class="abs" style="left:892px;top:128px;width:260px;font-size:14px;line-height:22px">Lorem Ipsum is simply dummy text of the printing and typesetting industry.</p>
  <div class="email-box">Email Address</div>
  <div class="btn" style="left:892px;top:254px;width:270px;height:56px">Subscribe now</div>

  <div class="bottom"><span>Copyright © 2019 Tavok Construction. All Right Reserved</span><span>Privacy Policy - Terms &amp; conditions</span></div>
</footer>

</body>
</html>
```